Tovek - Business Card Design

Design a modern masculine business card for our business

Target Market(s)

Private Market

Industry/Entity Type

Construction

Contact Information for Business Card

Company Name - Name of Person - Address - email address - contact number

Font styles to use
Serif
Sans Serif

Colors
0094D4
00A9DD
6FCCEA
C7EBF8
E9F6FB
00AB8E
00BBA5
67D7C9
C6EFE9
E9F9F6
F0912C
F2A743
F7CA91
FBE8D2
FDF5EE

Requirements
Must have
• Use company logo provided
Nice to have
• Company Logo

```html
<!DOCTYPE html>
<html lang="en">
<head>
<meta charset="utf-8">
<title>Tovek Construction – Business Card</title>
<link rel="stylesheet" href="https://fonts.googleapis.com/css2?family=Open+Sans:wght@400;600;700&display=swap">
<style>
  :root {
    --card-dark: #222227;
    --accent-orange: #ee6f2a;
    --text-white: #ffffff;
    --text-soft: #e6e6e6;
    --divider: #8a8a8f;
    --backdrop: #ecebe8;
    --shadow: rgba(0, 0, 0, 0.28);
  }
  * { box-sizing: border-box; margin: 0; padding: 0; }
  html, body {
    width: 1200px;
    height: 780px;
    overflow: hidden;
    background: var(--backdrop);
    font-family: "Open Sans", Arial, sans-serif;
  }
  .canvas {
    position: relative;
    width: 1200px;
    height: 780px;
  }
  .card {
    position: absolute;
    width: 620px;
    height: 354px;
    background: var(--card-dark);
    border-radius: 4px;
    box-shadow: 0 14px 30px var(--shadow);
    overflow: hidden;
  }
  .card--front { left: 120px; top: 30px; }
  .card--back  { left: 460px; top: 396px; }

  /* Wordmark */
  .wordmark {
    position: absolute;
    display: flex;
    align-items: center;
    gap: 14px;
    color: var(--text-white);
    font-weight: 700;
  }
  .wordmark__square {
    background: var(--accent-orange);
    flex: none;
  }
  .wordmark__text { line-height: 1; }
  .wordmark__name { display: block; text-transform: uppercase; letter-spacing: 2px; }
  .wordmark__sub  { display: block; text-transform: uppercase; letter-spacing: 2px; margin-top: 6px; }

  .card--front .wordmark { left: 50%; top: 50%; transform: translate(-50%, -50%); }
  .card--front .wordmark__square { width: 54px; height: 54px; }
  .card--front .wordmark__name { font-size: 76px; }
  .card--front .wordmark__sub  { font-size: 17px; }

  .card--back .wordmark { left: 206px; top: 40px; }
  .card--back .wordmark__square { width: 36px; height: 36px; }
  .card--back .wordmark__name { font-size: 50px; }
  .card--back .wordmark__sub  { font-size: 12px; margin-top: 4px; }

  /* Person */
  .person {
    position: absolute;
    left: 60px;
    top: 178px;
    width: 230px;
    text-align: right;
  }
  .person__name { font-size: 28px; font-weight: 700; line-height: 1.1; }
  .person__first { color: var(--accent-orange); }
  .person__last  { color: var(--text-white); }
  .person__title { color: var(--text-soft); font-size: 16px; margin-top: 4px; }

  .divider {
    position: absolute;
    left: 316px;
    top: 160px;
    width: 1px;
    height: 96px;
    background: var(--divider);
  }

  /* Contacts */
  .contacts {
    position: absolute;
    left: 342px;
    top: 164px;
    list-style: none;
  }
  .contacts__item {
    display: flex;
    align-items: center;
    gap: 12px;
    color: var(--text-white);
    font-size: 15px;
    height: 29px;
  }
  .contacts__icon { width: 16px; height: 16px; flex: none; fill: var(--accent-orange); }

  /* Address band */
  .address-band {
    position: absolute;
    left: 0;
    right: 0;
    top: 268px;
    height: 44px;
    background: var(--accent-orange);
    color: var(--text-white);
    font-size: 15px;
    display: flex;
    align-items: center;
    justify-content: center;
    letter-spacing: 0.3px;
  }
</style>
</head>
<body>
<main class="canvas">

  <section class="card card--front" aria-label="Business card front">
    <div class="wordmark">
      <span class="wordmark__square"></span>
      <span class="wordmark__text">
        <span class="wordmark__name">Tovek</span>
        <span class="wordmark__sub">Construction, Inc</span>
      </span>
    </div>
  </section>

  <section class="card card--back" aria-label="Business card back">
    <div class="wordmark">
      <span class="wordmark__square"></span>
      <span class="wordmark__text">
        <span class="wordmark__name">Tovek</span>
        <span class="wordmark__sub">Construction, Inc</span>
      </span>
    </div>

    <div class="person">
      <p class="person__name"><span class="person__first">Marta</span> <span class="person__last">Holub</span></p>
      <p class="person__title">Managing Director</p>
    </div>

    <span class="divider"></span>

    <ul class="contacts">
      <li class="contacts__item">
        <svg class="contacts__icon" viewBox="0 0 24 24" aria-hidden="true"><path d="M6.6 10.8a15.1 15.1 0 0 0 6.6 6.6l2.2-2.2a1 1 0 0 1 1-.25 11.4 11.4 0 0 0 3.6.57 1 1 0 0 1 1 1V20a1 1 0 0 1-1 1A17 17 0 0 1 3 4a1 1 0 0 1 1-1h3.5a1 1 0 0 1 1 1c0 1.25.2 2.45.57 3.6a1 1 0 0 1-.25 1z"/></svg>
        (555) 214-0387
      </li>
      <li class="contacts__item">
        <svg class="contacts__icon" viewBox="0 0 24 24" aria-hidden="true"><path d="M2 5h20v14H2zm2 2v.4l8 5.2 8-5.2V7zm0 2.8V17h16V9.8l-8 5.2z"/></svg>
        info@tovekbuild.com
      </li>
      <li class="contacts__item">
        <svg class="contacts__icon" viewBox="0 0 24 24" aria-hidden="true"><path d="M12 2a10 10 0 1 0 0 20 10 10 0 0 0 0-20zm6.9 6h-3a15.6 15.6 0 0 0-1.4-3.6A8 8 0 0 1 18.9 8zM12 4c.8 1.2 1.5 2.5 1.9 4h-3.8c.4-1.5 1.1-2.8 1.9-4zM4.3 14a8.2 8.2 0 0 1 0-4h3.4a16 16 0 0 0 0 4zm.8 2h3a15.6 15.6 0 0 0 1.4 3.6A8 8 0 0 1 5.1 16zm3-8h-3a8 8 0 0 1 4.4-3.6A15.6 15.6 0 0 0 8.1 8zM12 20c-.8-1.2-1.5-2.5-1.9-4h3.8c-.4 1.5-1.1 2.8-1.9 4zm2.3-6H9.7a14.7 14.7 0 0 1 0-4h4.6a14.7 14.7 0 0 1 0 4zm.2 5.6a15.6 15.6 0 0 0 1.4-3.6h3a8 8 0 0 1-4.4 3.6zm1.8-5.6a16 16 0 0 0 0-4h3.4a8.2 8.2 0 0 1 0 4z"/></svg>
        www.tovekbuild.com
      </li>
    </ul>

    <p class="address-band">4218 Brennan Ct #204, Cedar Bay, FL 32011, USA</p>
  </section>

</main>
</body>
</html>
```